Web Design Business Card

I need a new business card designed, we recently rebranded and I need to get a fresh design to match our new logo, colours and branding.

Details:

Dorian Keeble | Founder & CEO
Address: 7 Fernhollow Lane, #04-09 Maplecrest Vale, Singapore 583104
Tel: +65 93468120
Web: www.plumtrove.com.sg
hello@plumtrove.com.sg

I've attached my old card as well

Requirements
Must have
• Front and Back
Interesting use of logo
Correct use of colour scheme

```html
<!DOCTYPE html>
<html lang="en">
<head>
<meta charset="utf-8">
<title>Plumtrove Business Card</title>
<link rel="stylesheet" href="https://fonts.googleapis.com/css2?family=Mulish:wght@400;600;700;800&display=swap">
<style>
  :root {
    --backdrop: #4b4b4d;
    --card-white: #f4f4f3;
    --card-brown: #67594f;
    --card-brown-dark: #5a4d44;
    --brand-blue: #1a9bdc;
    --brand-blue-light: #5cc0ef;
    --brand-brown: #6b5d53;
    --text-gray: #5d5550;
    --rule: #cfcac6;
    --name-light: #efecea;
  }
  html, body {
    margin: 0;
    padding: 0;
    width: 1200px;
    height: 1000px;
    overflow: hidden;
    background: var(--backdrop);
    font-family: "Mulish", sans-serif;
  }
  .canvas { position: relative; width: 1200px; height: 1000px; }
  .card {
    position: absolute;
    width: 530px;
    height: 303px;
    border-radius: 14px;
    overflow: hidden;
  }
  .card--front { left: 165px; top: 163px; background: var(--card-white); }
  .card--back {
    left: 473px; top: 549px;
    background: linear-gradient(135deg, var(--card-brown), var(--card-brown-dark));
  }
  .brand { position: absolute; }
  .brand__dot {
    position: absolute;
    width: 66px; height: 66px;
    border-radius: 50%;
    background: linear-gradient(180deg, var(--brand-blue), var(--brand-blue-light));
  }
  .brand__name {
    position: absolute;
    font-weight: 700;
    font-size: 34px;
    line-height: 1;
    letter-spacing: -0.6px;
    white-space: nowrap;
  }
  .brand__tagline {
    position: absolute;
    font-weight: 800;
    font-size: 9.6px;
    letter-spacing: 0.2px;
    color: var(--brand-blue);
    white-space: nowrap;
  }
  .card--front .brand { left: 28px; top: 121px; }
  .card--front .brand__dot { left: 0; top: 0; }
  .card--front .brand__name { left: 77px; top: 11px; color: var(--brand-brown); }
  .card--front .brand__tagline { left: 78px; top: 50px; }
  .card--back .brand { left: 147px; top: 114px; }
  .card--back .brand__dot { left: 0; top: 0; }
  .card--back .brand__name { left: 78px; top: 11px; color: var(--name-light); }
  .card--back .brand__tagline { left: 79px; top: 50px; }

  .divider {
    position: absolute;
    left: 291px; top: 86px;
    width: 1px; height: 136px;
    background: var(--rule);
  }
  .contact { position: absolute; left: 320px; top: 82px; color: var(--text-gray); }
  .contact__name {
    margin: 0;
    font-weight: 800;
    font-size: 16px;
    letter-spacing: 0.3px;
    color: var(--brand-blue);
  }
  .contact__role { margin: 1px 0 8px; font-size: 12px; }
  .contact__list { list-style: none; margin: 0; padding: 0; }
  .contact__item {
    display: flex; align-items: center;
    height: 18px;
    font-size: 12px;
  }
  .contact__item svg { width: 13px; height: 13px; margin-right: 12px; }
  .contact__address {
    margin: 8px 0 0;
    font-size: 12px;
    line-height: 16px;
    letter-spacing: -0.15px;
  }
</style>
</head>
<body>
<main class="canvas">
  <section class="card card--front" aria-label="Card front">
    <div class="brand">
      <span class="brand__dot"></span>
      <span class="brand__name">plumtrove</span>
      <span class="brand__tagline">WEB DESIGN &amp; CONSULTANCY</span>
    </div>
    <span class="divider"></span>
    <div class="contact">
      <h1 class="contact__name">DORIAN KEEBLE</h1>
      <p class="contact__role">Founder &amp; CEO</p>
      <ul class="contact__list">
        <li class="contact__item">
          <svg viewBox="0 0 14 14" aria-hidden="true"><circle cx="7" cy="7" r="6.2" fill="none" stroke="#1a9bdc" stroke-width="1.1"/><path d="M4.6 3.8l1.3 0.2 0.5 1.6-0.8 0.7c0.4 0.9 1 1.5 1.9 1.9l0.7-0.8 1.6 0.5 0.2 1.3c-2.9 0.6-5.9-2.4-5.3-5.4z" fill="#1a9bdc"/></svg>
          +65 93468120
        </li>
        <li class="contact__item">
          <svg viewBox="0 0 14 14" aria-hidden="true"><circle cx="7" cy="7" r="6.2" fill="none" stroke="#1a9bdc" stroke-width="1.1"/><rect x="3.6" y="4.6" width="6.8" height="4.8" fill="none" stroke="#1a9bdc" stroke-width="1"/><path d="M3.6 4.8L7 7.4l3.4-2.6" fill="none" stroke="#1a9bdc" stroke-width="1"/></svg>
          hello@plumtrove.com.sg
        </li>
        <li class="contact__item">
          <svg viewBox="0 0 14 14" aria-hidden="true"><g fill="none" stroke="#1a9bdc" stroke-width="1"><circle cx="7" cy="7" r="6.2"/><ellipse cx="7" cy="7" rx="2.6" ry="6.2"/><path d="M0.8 7h12.4M1.8 4h10.4M1.8 10h10.4"/></g></svg>
          www.plumtrove.com.sg
        </li>
      </ul>
      <p class="contact__address">7 Fernhollow Lane, #04-09<br>Maplecrest Vale, Singapore 583104</p>
    </div>
  </section>

  <section class="card card--back" aria-label="Card back">
    <div class="brand">
      <span class="brand__dot"></span>
      <span class="brand__name">plumtrove</span>
      <span class="brand__tagline">WEB DESIGN &amp; CONSULTANCY</span>
    </div>
  </section>
</main>
</body>
</html>
```